Letterhead and invoice

Simple design for letterhead and invoice document (2 separate files). Must be word and excel compatible.

Must use logo (attached)
ABN: 47 209 851 624
Address: 14 Marrick Crescent, Tolland NSW
Phone: 0417263948

Target Market(s)

Professional

Industry/Entity Type

Invoice

Font styles to use
Serif
Sans Serif

Colors

Designer to choose colors to be used in the design.

Requirements
Must have
• As above

```html
<!DOCTYPE html>
<html lang="en">
<head>
<meta charset="utf-8">
<title>Brennan Earthworks Letterhead</title>
<link rel="stylesheet" href="https://fonts.googleapis.com/css2?family=Lato:wght@400;900&display=swap">
<style>
  :root {
    --backdrop: #cbcccd;
    --paper: #ffffff;
    --brand-red: #e0262a;
    --ink: #1a1a1a;
    --rule: #6d6e70;
  }
  html, body {
    margin: 0;
    padding: 0;
    overflow: hidden;
  }
  body {
    width: 848px;
    height: 1200px;
    background: var(--backdrop);
    position: relative;
    font-family: "Lato", Arial, sans-serif;
  }
  .sheet {
    position: absolute;
    left: 57px;
    top: 81px;
    width: 732px;
    height: 1036px;
    background: var(--paper);
  }
  .brand {
    position: absolute;
    left: 41px;
    top: 30px;
    height: 40px;
    display: flex;
    align-items: center;
    gap: 12px;
  }
  .brand-square {
    width: 40px;
    height: 40px;
    background: var(--brand-red);
  }
  .brand-name {
    font-weight: 900;
    font-size: 21px;
    letter-spacing: 0.3px;
    text-transform: uppercase;
    color: var(--ink);
    line-height: 1;
  }
  .contact {
    position: absolute;
    left: 500px;
    top: 22px;
    padding-left: 13px;
    border-left: 1.5px solid var(--rule);
    font-size: 13px;
    line-height: 16px;
    color: var(--ink);
  }
  .contact p {
    margin: 0;
  }
</style>
</head>
<body>
  <main class="sheet">
    <header>
      <div class="brand">
        <span class="brand-square" aria-hidden="true"></span>
        <span class="brand-name">Brennan Earthworks</span>
      </div>
      <address class="contact" style="font-style: normal;">
        <p>ABN: 47 209 851 624</p>
        <p>Phone: 0417 263 948</p>
        <p>Address: 14 Marrick Crescent,<br>Tolland NSW</p>
        <p>Email: brennanearthworks@mail.com</p>
      </address>
    </header>
  </main>
</body>
</html>
```